Need a Car Magnet designed

I need a car magnet designed.

The dimensions have to be 9" width by 2.6" height.

It needs to say BLORVIK TOUR and include the attached logo

```html
<!DOCTYPE html>
<html lang="en">
<head>
<meta charset="utf-8">
<title>BLORVIK TOUR – Car Magnet</title>
<link href="https://fonts.googleapis.com/css2?family=Archivo+Black&display=swap" rel="stylesheet">
<style>
  :root {
    --page-grey: #e4e4e4;
    --magnet-navy: #1c3272;
    --ray-light: #2f63b8;
    --ray-dark: #1b3f92;
    --title-white: #ffffff;
    --paper-white: #ffffff;
    --mark-blue: #1e3f94;
    --mark-red: #d4232c;
  }
  html, body {
    margin: 0;
    width: 1200px;
    height: 600px;
    overflow: hidden;
    background: var(--page-grey);
  }
  .car-magnet {
    display: block;
    width: 1200px;
    height: 600px;
  }
  .magnet-body { fill: var(--magnet-navy); }
  .inner-rule { fill: none; stroke: var(--paper-white); stroke-width: 3; }
  .logo-panel { fill: var(--paper-white); }
  .logo-dot { fill: var(--mark-red); }
  .logo-name {
    font-family: "Archivo Black", sans-serif;
    font-size: 22px;
    fill: var(--mark-blue);
    text-anchor: middle;
  }
  .title-line {
    font-family: "Archivo Black", sans-serif;
    font-size: 112px;
    fill: var(--title-white);
    text-anchor: middle;
  }
</style>
</head>
<body>
<svg class="car-magnet" viewBox="0 0 1200 600" xmlns="http://www.w3.org/2000/svg">
  <defs>
    <radialGradient id="raysGlow" cx="0.45" cy="0.5" r="0.7">
      <stop offset="0" stop-color="var(--ray-light)"/>
      <stop offset="1" stop-color="var(--ray-dark)"/>
    </radialGradient>
  </defs>

  <rect class="magnet-body" x="50" y="145" width="1100" height="313" rx="10"/>
  <rect x="62" y="157" width="1076" height="289" fill="url(#raysGlow)"
        role="img" aria-label="Blue sunburst rays radiating behind the title"/>
  <rect class="inner-rule" x="62" y="157" width="1076" height="289"/>

  <rect class="logo-panel" x="117" y="159" width="150" height="285"/>
  <g class="tour-mark">
    <circle class="logo-dot" cx="192" cy="262" r="24"/>
    <text class="logo-name" x="192" y="322">BLORVIK</text>
    <text class="logo-name" x="192" y="350">TOUR</text>
  </g>

  <g class="title">
    <text class="title-line" x="720" y="286" textLength="560" lengthAdjust="spacingAndGlyphs">BLORVIK</text>
    <text class="title-line" x="720" y="408" textLength="380" lengthAdjust="spacingAndGlyphs">TOUR</text>
  </g>
</svg>
</body>
</html>
```